Build a Web page - Dovin Pratchell Homes, LLC - a custom home builder

We are a custom home builder in Wisconsin. Need a basic web page with a home page, About Us, Contact info, Gallery, and Testimonials page. Gallery will probably have sub-pages and each will have about ten pictures or less. I already own the domain and have web hosting through Wix, I just need the site built. Once the page is built I should be able to do the upkeep on it myself. If I need to add pictures or whatever.
Updates

Project Deadline Extended
Reason: I am still looking through designs and will select soon - thank you!

Target Market(s)

Gen X and Millennials who are looking to build a home. Custom built homes - not generic spec homes.

Industry/Entity Type

Home Builder

Number of Pages Required

5+ page

Font styles to use
Sans Serif

Colors
ffffff
ec1f27
000000
9d9d9d

Requirements
Must have
• I have no idea if I want coded or in coded. I'm not sure of the difference and why I would want one over the other.
Nice to have
• We like the following colors - red, black, gray, white.
Should not have
• not a big fan of clip art like hammers, tape measures, etc. Must look professional.

```html
<!DOCTYPE html>
<html lang="en">
<head>
<meta charset="utf-8">
<title>Dovin Pratchell Homes, LLC</title>
<link href="https://fonts.googleapis.com/css2?family=Roboto:ital,wght@0,300;0,400;0,500;0,700;1,500&display=swap" rel="stylesheet">
<style>
:root{
  --red:#9e1b21;
  --red-dark:#8a161b;
  --red-bright:#c8262d;
  --ink:#222;
  --text:#555;
  --muted:#9d9d9d;
  --light:#f2f2f2;
  --footer:#3c3c3c;
  --white:#fff;
  --yellow:#e8d54a;
}
*{box-sizing:border-box;margin:0;padding:0}
html,body{width:1200px;height:2956px;overflow:hidden}
body{font-family:'Roboto',sans-serif;color:var(--text);background:var(--white);position:relative}
a{color:inherit;text-decoration:none}
.abs{position:absolute}

/* top bar */
.topbar{top:0;left:0;width:1200px;height:28px;background:#f7f7f7;border-bottom:1px solid #e4e4e4}
.topbar .ask{left:162px;top:6px;font-size:12px;color:var(--red);display:flex;align-items:center;gap:8px}
.topbar .social{right:162px;top:6px;display:flex;gap:8px}
.dot{width:12px;height:12px;background:#555;border-radius:2px}

/* header */
.header{top:28px;left:0;width:1200px;height:130px;background:var(--white)}
.brand{left:162px;top:12px;width:88px;height:80px;border:3px solid #999;display:flex;align-items:center;justify-content:center;text-align:center;font-size:11px;font-weight:700;color:var(--red);line-height:1.2;padding:4px}
.info{top:28px;display:flex;gap:10px;font-size:11px;color:#666;line-height:1.35}
.info b{display:block;color:var(--red);font-size:14px;font-weight:700}
.info .big{font-size:21px;color:var(--ink);font-weight:500}
.info svg{flex:none}

/* nav */
.nav{top:138px;left:162px;width:874px;height:52px;background:var(--red);display:flex;align-items:center;padding:0 20px;z-index:3;box-shadow:0 2px 4px rgba(0,0,0,.25)}
.nav a{color:var(--white);font-size:12px;font-weight:500;margin-right:86px}
.nav .quote{position:absolute;right:10px;top:10px;height:32px;background:var(--white);color:var(--ink);border-radius:3px;padding:0 14px;display:flex;align-items:center;gap:6px;font-size:12px;margin:0}

/* hero */
.hero{top:158px;left:0;width:1200px;height:492px;background:linear-gradient(180deg,#8d9099 0%,#7a6d60 45%,#5d6a3a 80%,#4c6a2d 100%)}
.hero .copy{left:0;top:150px;width:1200px;text-align:center;color:var(--white)}
.hero h1{font-size:60px;font-weight:700;letter-spacing:-2px;text-shadow:0 2px 6px rgba(0,0,0,.4)}
.hero h2{font-size:33px;font-weight:300;margin-top:-4px}
.hero p{font-size:11px;width:700px;margin:12px auto 0;line-height:1.5}
.hero .more{display:inline-flex;align-items:center;gap:6px;margin-top:26px;background:var(--red-bright);padding:8px 16px;border-radius:16px;font-size:13px}
.arrow{top:215px;font-size:40px;color:var(--white);font-weight:300}

/* section heads */
.sechead{left:0;width:1200px;text-align:center}
.sechead h3{font-size:36px;font-weight:500;color:var(--ink);letter-spacing:1px}
.sechead h3 span{color:var(--red)}
.sechead .sub{font-size:13px;color:var(--red);font-weight:700;margin-top:6px}
.sechead p{font-size:11px;width:780px;margin:14px auto 0;line-height:1.55;color:#666}

/* cards */
.card{top:828px;width:276px;height:394px;border:2px solid var(--red);background:var(--white)}
.card .photo{height:176px;border-bottom:2px solid var(--red)}
.card .body{padding:18px 8px 0 8px;background:#f6f6f6;height:174px}
.card h4{font-size:13px;color:var(--red);font-weight:500;line-height:1.35;text-transform:uppercase}
.card .type{font-size:12px;color:#777;margin-top:4px}
.card .spec{font-size:10px;color:#555;margin-top:14px;line-height:1.5}
.card .price{font-size:19px;color:var(--red);font-weight:500;margin-top:12px}
.card .foot{height:40px;display:flex;border-top:1px solid #ddd}
.card .foot div{display:flex;align-items:center;font-size:11px;gap:6px;padding:0 10px}
.card .foot .view{width:150px;border-right:1px solid #ddd;color:#333}
.card .foot .prop{color:var(--red)}
.pill{width:16px;height:16px;border-radius:50%}

/* features */
.features{top:1267px;left:0;width:1200px;height:443px}
.features .photo{left:0;top:0;width:587px;height:443px;background:linear-gradient(180deg,#8fb2d9 0%,#c4d4e2 35%,#6b7260 55%,#4f7a33 75%,#5f8e3a 100%)}
.features .panel{left:587px;top:0;width:613px;height:443px;background:var(--red);color:var(--white);padding:40px 30px}
.features .kicker{font-size:14px;font-weight:500}
.features h3{font-size:35px;font-weight:500;margin-top:2px}
.feat-grid{display:grid;grid-template-columns:210px 210px;column-gap:8px;row-gap:22px;margin-top:24px}
.feat h5{font-size:18px;font-weight:400;margin-top:4px}
.feat p{font-size:9.5px;line-height:1.5;margin-top:6px;opacity:.9}

/* gallery */
.gallery-row{top:1864px;left:0;width:1200px;height:297px;display:flex;gap:4px}
.gallery-row div{flex:1}
.g1{background:linear-gradient(180deg,#c9bfae,#8a5a2e 55%,#3d2a1d)}
.g2{background:linear-gradient(180deg,#7ea5d6,#b7c6d4 35%,#5c6950 55%,#5f913c)}
.g3{background:linear-gradient(180deg,#cfd5dc,#9c8a76 50%,#5f8a3a)}
.g4{background:linear-gradient(180deg,#e9e6de,#a0683d 60%,#d9d2c6)}
.gnav{top:2000px;width:28px;height:28px;background:var(--red);color:var(--white);display:flex;align-items:center;justify-content:center;font-size:14px}

/* testimonial */
.testi{top:2226px;left:0;width:565px;height:434px;background:var(--light);padding:0 0 0 160px}
.testi .btns{position:absolute;left:488px;top:22px;display:flex;gap:4px}
.testi .btns span{width:24px;height:22px;background:var(--red);color:var(--white);font-size:13px;display:flex;align-items:center;justify-content:center}
.testi h3{position:absolute;left:160px;top:60px;font-size:29px;font-weight:400;color:#444}
.testi h3 span{color:var(--red)}
.testi h3::after{content:"";display:block;width:40px;height:2px;background:var(--red);margin-top:4px}
.avatar{left:160px;top:130px;width:134px;height:134px;border-radius:50%;border:3px solid var(--red);background:radial-gradient(circle at 50% 45%,#d8c0b0,#6e4a3a 70%,#2a1a15)}
.testi .who{position:absolute;left:310px;top:160px}
.testi .who h4{font-size:17px;font-weight:400;color:#333}
.testi .who small{font-size:11px;color:#777}
.stars{color:#f0a500;font-size:12px;letter-spacing:1px}
.testi p.quote{position:absolute;left:160px;top:282px;width:380px;font-size:11px;line-height:1.65;color:#555}
.testi .sign{position:absolute;left:160px;top:372px;font-size:13px;color:var(--red)}

/* quick search */
.search{top:2226px;left:565px;width:635px;height:434px;background:var(--red);color:var(--white);padding:38px 20px 0 20px}
.search h3{text-align:center;font-size:38px;font-weight:500}
.search .grid{display:grid;grid-template-columns:repeat(3,188px);column-gap:10px;row-gap:14px;margin-top:30px}
.field label{display:block;font-size:12px;font-weight:500;margin-bottom:8px}
.sel{height:32px;background:var(--white);color:#888;font-size:10px;display:flex;align-items:center;justify-content:space-between;padding:0 8px;border-radius:2px}
.sel::after{content:"";width:6px;height:6px;border-right:1.5px solid #444;border-bottom:1.5px solid #444;transform:rotate(45deg) translateY(-2px)}
.search .go{display:block;margin:26px auto 0;width:230px;height:28px;background:var(--yellow);color:#333;font-size:10px;font-weight:700;text-align:center;line-height:28px}

/* footer */
.footer{top:2660px;left:0;width:1200px;height:248px;background:var(--footer);color:#ddd}
.footer .brand{left:162px;top:46px;border-color:#ccc;background:var(--white)}
.footer .about{left:162px;top:138px;width:260px;font-size:10px;line-height:1.55;color:#ddd}
.footer h4{font-size:17px;font-weight:500;font-style:italic;color:var(--white)}
.footer h4::after{content:"";display:block;width:40px;height:2px;background:var(--red-bright);margin-top:4px}
.links{left:543px;top:54px}
.links ul{list-style:none;margin-top:14px}
.links li{font-size:12px;margin-bottom:12px;display:flex;align-items:center;gap:8px}
.links li::before{content:"";width:7px;height:7px;border:2px solid #ddd;border-radius:50%}
.contact{left:852px;top:54px;width:200px}
.contact .row{display:flex;gap:8px;font-size:10.5px;line-height:1.45;margin-top:12px}
.contact .socials{display:flex;gap:6px;margin-top:18px}
.contact .socials span{width:28px;height:24px;border:1px solid #bbb;background:#fff}
.bottom{top:2908px;left:0;width:1200px;height:48px;background:var(--red-dark);color:var(--white);font-size:11px;display:flex;align-items:center;padding:0 162px}
.bottom a{margin-right:46px}
.bottom .circles{margin-left:auto;display:flex;gap:8px}
.bottom .circles span{width:20px;height:20px;border:1.5px solid #fff;border-radius:50%}
</style>
</head>
<body>

<div class="abs topbar">
  <div class="abs ask">
    <svg width="14" height="12" viewBox="0 0 14 12"><path d="M1 1h12v7H6l-3 3V8H1z" fill="none" stroke="currentColor" stroke-width="1.4"/></svg>
    Feel free to ask any qauestion
  </div>
  <div class="abs social"><span class="dot"></span><span class="dot"></span><span class="dot"></span><span class="dot"></span></div>
</div>

<header class="abs header">
  <div class="abs brand">Dovin Pratchell Homes, LLC</div>
  <div class="abs info" style="left:460px">
    <svg width="14" height="20" viewBox="0 0 14 20"><path d="M7 1a6 6 0 0 0-6 6c0 4.5 6 12 6 12s6-7.5 6-12a6 6 0 0 0-6-6z" fill="none" stroke="#9e1b21" stroke-width="1.5"/><circle cx="7" cy="7" r="2" fill="#9e1b21"/></svg>
    <div><b>ADDRESS:</b>Lorem Ipsum is simply dummy<br>text of the printing...</div>
  </div>
  <div class="abs info" style="left:678px">
    <svg width="12" height="20" viewBox="0 0 12 20"><rect x="1" y="1" width="10" height="18" rx="2" fill="none" stroke="#9e1b21" stroke-width="1.5"/><circle cx="6" cy="15.5" r="1" fill="#9e1b21"/></svg>
    <div><b>PHONE:</b><span class="big">888-555-0142</span></div>
  </div>
  <div class="abs info" style="left:898px">
    <svg width="20" height="14" viewBox="0 0 20 14"><rect x="1" y="1" width="18" height="12" fill="none" stroke="#9e1b21" stroke-width="1.5"/><path d="M1 1l9 7 9-7" fill="none" stroke="#9e1b21" stroke-width="1.5"/></svg>
    <div><b>EMAIL US NOW:</b>info@dovinpratchell.com</div>
  </div>
</header>

<section class="abs hero" role="img" aria-label="Photo of a stone and siding family home with a green lawn and bare trees">
  <div class="abs copy">
    <h1>We Plan for your Success</h1>
    <h2>The best way to find your home</h2>
    <p>Lorem Ipsum is simply dummy text of the printing and typesetting industry. Lorem Ipsum has been the industry's standard dummy text ever since the 1500s, when an unknown printer took a galley...</p>
    <a class="more" href="#"><svg width="12" height="12" viewBox="0 0 12 12"><circle cx="6" cy="6" r="6" fill="#fff"/><path d="M5 3l3 3-3 3" fill="none" stroke="#c8262d" stroke-width="1.6"/></svg>Read More...</a>
  </div>
  <span class="abs arrow" style="left:20px">&#8249;</span>
  <span class="abs arrow" style="right:20px">&#8250;</span>
</section>

<nav class="abs nav">
  <a href="#">HOME</a><a href="#">ABOUT US</a><a href="#">GALLERY</a><a href="#">TESTIMONIALS</a><a href="#">CONTACT US</a>
  <a class="quote" href="#"><svg width="12" height="12" viewBox="0 0 12 12"><circle cx="6" cy="6" r="6" fill="#9e1b21"/><path d="M5 3l3 3-3 3" fill="none" stroke="#fff" stroke-width="1.6"/></svg>GET A QUOTE</a>
</nav>

<section class="abs sechead" style="top:688px">
  <h3>REAL ESTATES</h3>
  <div class="sub">DOVIN PRATCHELL HOMES</div>
  <p>Lorem Ipsum is simply dummy text of the printing and typesetting industry. Lorem Ipsum has been the industry's standard dummy text ever since the 1500s, when an unknown printer took a galley of type and scrambled it to make a type specimen book.</p>
</section>

<article class="abs card" style="left:162px">
  <div class="photo" role="img" aria-label="Photo of a two-storey tan siding house" style="background:linear-gradient(180deg,#d6dde4,#8b8a80 55%,#6f8a4a)"></div>
  <div class="body"><h4>Sell beautiful home in one of the best areas</h4><div class="type">Multi Family House1800 sq ft</div><div class="spec">Built: 2010 Area: 1800 sq ft<br>Beds: 4 Baths: 3 Garages: 2 (4 auto)</div><div class="price">$849,000</div></div>
  <div class="foot"><div class="view">&#9679; VIEW DETAILS</div><div class="prop">Property: <span class="pill" style="background:#e05a5a"></span><span class="pill" style="background:#333"></span></div></div>
</article>
<article class="abs card" style="left:461px">
  <div class="photo" role="img" aria-label="Photo of a back deck on a cream-coloured house" style="background:linear-gradient(180deg,#e4e1d6,#c9c3b0 45%,#7d3b32 75%,#6f8a4a)"></div>
  <div class="body"><h4>Sell beautiful home in one of the best areas</h4><div class="type">Multi Family House1800 sq ft</div><div class="spec">Built: 2010 Area: 1800 sq ft<br>Beds: 4 Baths: 3 Garages: 2 (4 auto)</div><div class="price">$849,000</div></div>
  <div class="foot"><div class="view">&#9679; VIEW DETAILS</div><div class="prop">Property: <span class="pill" style="background:#e05a5a"></span><span class="pill" style="background:#333"></span></div></div>
</article>
<article class="abs card" style="left:761px">
  <div class="photo" role="img" aria-label="Photo of a green ranch house with a three-car garage" style="background:linear-gradient(180deg,#7ea5d6,#b7c6d4 40%,#5c6950 60%,#5f913c)"></div>
  <div class="body"><h4>Sell beautiful home in one of the best areas</h4><div class="type">Multi Family House1800 sq ft</div><div class="spec">Built: 2010 Area: 1800 sq ft<br>Beds: 4 Baths: 3 Garages: 2 (4 auto)</div><div class="price">$849,000</div></div>
  <div class="foot"><div class="view">&#9679; VIEW DETAILS</div><div class="prop">Property: <span class="pill" style="background:#e05a5a"></span><span class="pill" style="background:#333"></span></div></div>
</article>

<section class="abs features">
  <div class="abs photo" role="img" aria-label="Photo of a green two-storey home with stone front and white garage doors"></div>
  <div class="abs panel">
    <div class="kicker">DOVIN PRATCHELL HOMES</div>
    <h3>FEATURES SERVICES</h3>
    <div class="feat-grid">
      <div class="feat">
        <svg width="34" height="38" viewBox="0 0 34 38"><path d="M12 2h10l-3 6h-4z" fill="#fff"/><path d="M15 9h4c8 4 13 12 13 18 0 6-6 9-15 9S2 33 2 27c0-6 5-14 13-18z" fill="#fff"/><text x="17" y="29" text-anchor="middle" font-size="14" font-weight="700" fill="#9e1b21" font-family="Roboto,sans-serif">$</text></svg>
        <h5>Save Money</h5><p>Lorem Ipsum is simply dummy text of the printing and typesetting industry. Lorem Ipsum has been...</p>
      </div>
      <div class="feat">
        <svg width="44" height="38" viewBox="0 0 44 38"><rect x="4" y="24" width="6" height="12" fill="#fff"/><rect x="14" y="18" width="6" height="18" fill="#fff"/><rect x="24" y="22" width="6" height="14" fill="#fff"/><rect x="34" y="12" width="6" height="24" fill="#fff"/><path d="M4 16l10-8 10 6 14-12" fill="none" stroke="#fff" stroke-width="2.5"/></svg>
        <h5>Good sales &amp; marketing</h5><p>Lorem Ipsum is simply dummy text of the printing and typesetting industry. Lorem Ipsum has been...</p>
      </div>
      <div class="feat">
        <svg width="40" height="30" viewBox="0 0 40 30"><path d="M2 10l10 10 8-6 8 6 10-10" fill="none" stroke="#fff" stroke-width="4" stroke-linejoin="round"/><path d="M12 20l6 6h6l4-4" fill="none" stroke="#fff" stroke-width="3"/></svg>
        <h5>Comfort</h5><p>Lorem Ipsum is simply dummy text of the printing and typesetting industry. Lorem Ipsum has been...</p>
      </div>
      <div class="feat">
        <svg width="30" height="30" viewBox="0 0 30 30"><circle cx="12" cy="12" r="8" fill="none" stroke="#fff" stroke-width="3.5"/><path d="M18 18l8 8" stroke="#fff" stroke-width="4.5" stroke-linecap="round"/></svg>
        <h5>Easy to Find</h5><p>Lorem Ipsum is simply dummy text of the printing and typesetting industry. Lorem Ipsum has been...</p>
      </div>
    </div>
  </div>
</section>

<section class="abs sechead" style="top:1748px">
  <h3><span>OUR</span> GALLERY</h3>
  <p>Lorem Ipsum is simply dummy text of the printing and typesetting industry. Lorem Ipsum has been the industry's standard dummy text ever since the 1500s, when an unknown printer took a galley of type and scrambled it to make a type specimen book.</p>
</section>

<div class="abs gallery-row">
  <div class="g1" role="img" aria-label="Photo of a wooden mudroom locker bench"></div>
  <div class="g2" role="img" aria-label="Photo of a green home with driveway and garage"></div>
  <div class="g3" role="img" aria-label="Photo of a tan ranch home with a walkway"></div>
  <div class="g4" role="img" aria-label="Photo of a wooden staircase with white walls"></div>
</div>
<span class="abs gnav" style="left:0">&#8592;</span>
<span class="abs gnav" style="right:0">&#8594;</span>

<section class="abs testi">
  <div class="btns"><span>&#8592;</span><span>&#8594;</span></div>
  <h3>Client <span>Testimonial</span></h3>
  <div class="abs avatar" role="img" aria-label="Portrait photo of the client"></div>
  <div class="who"><h4>Real Estate is best choice</h4><small>Lena Varsik (Business Developer)</small><div class="stars">&#9733;&#9733;&#9733;&#9733;&#9733;</div></div>
  <p class="quote">Lorem Ipsum is simply dummy text of the printing and typesetting industry. Lorem Ipsum has been the industry's standard dummy text ever since the 1500s, when an unknown printer took a galley of type and scrambled it to make a type specimen book. It has survived no..</p>
  <div class="sign">Lena Varsik</div>
</section>

<section class="abs search">
  <h3>Quick Search</h3>
  <div class="grid">
    <div class="field"><label>PROPERTY LOCATION:</label><div class="sel">Any</div></div>
    <div class="field"><label>PROPERTY TYPE</label><div class="sel">Any</div></div>
    <div class="field"><label>PROPERTY FEATURE</label><div class="sel">Any</div></div>
    <div class="field"><label>BEDS:</label><div class="sel">No of Bed</div></div>
    <div class="field"><label>BATHROOMS:</label><div class="sel">No of Baths</div></div>
    <div class="field"><label>BUILT-UP AREA (SQ.FT)</label><div class="sel">2000 sqf</div></div>
    <div class="field"><label>MAX PRICE:</label><div class="sel">$500</div></div>
    <div class="field"><label>MIN PRICE:</label><div class="sel">$600</div></div>
    <div class="field"><label>MIN PRICE:</label><div class="sel">$600</div></div>
  </div>
  <a class="go" href="#">SEARCH</a>
</section>

<footer class="abs footer">
  <div class="abs brand">Dovin Pratchell Homes, LLC</div>
  <p class="abs about">Lorem Ipsum is simply dummy text of the printing and typesetting industry. Lorem Ipsum has been the industry's standard dummy text ever since the 1500s, when an unknown printer took a galley of type and scrambled it to make a type specimen book.</p>
  <div class="abs links">
    <h4>Quick Link</h4>
    <ul><li>Home</li><li>About Us</li><li>Gallery</li><li>Testimonials</li><li>Contact Us</li></ul>
  </div>
  <div class="abs contact">
    <h4>CONTACT US</h4>
    <div class="row"><svg width="10" height="14" viewBox="0 0 10 14"><path d="M5 0a5 5 0 0 0-5 5c0 4 5 9 5 9s5-5 5-9a5 5 0 0 0-5-5z" fill="#e0474e"/></svg><span>Address : Lorem Ipsum is simply dummy text of the printing...</span></div>
    <div class="row"><svg width="12" height="12" viewBox="0 0 12 12"><path d="M2 1l2 0 1 3-1.5 1a6 6 0 0 0 3.5 3.5L8 7l3 1v2a1 1 0 0 1-1 1A9 9 0 0 1 1 2a1 1 0 0 1 1-1z" fill="#e0474e"/></svg><span>Phone : 888-555-0142</span></div>
    <div class="row"><svg width="12" height="10" viewBox="0 0 12 10"><rect width="12" height="10" fill="#e0474e"/><path d="M0 0l6 5 6-5" fill="none" stroke="#3c3c3c"/></svg><span>Email : hello@dovinpratchell.com</span></div>
    <div class="socials"><span></span><span></span><span></span></div>
  </div>
</footer>

<div class="abs bottom">
  <a href="#">Home</a><a href="#">About Us</a><a href="#">Gallery</a><a href="#">Testimonials</a><a href="#">Contact Us</a>
  <div class="circles"><span></span><span></span><span></span><span></span><span></span></div>
</div>

</body>
</html>
```